A Health & Fitness Website selling saunas and Cold tubs

www.tarnwellgear.com, www.frostvaleco, www.brimholdsupply
Design a website
We are selling saunas, infrared saunas, cold plunge tubs, and massage chairs to financially successful MEN.
We want professional, simple, masculine with a touch of sexy.
One section for each… saunas, cold plunge tubs, massage chairs.
Each will have at least two buy links to their affiliate/supplier/store.
The landing page / opening page / needs big & bold; a full screen image? a great picture showing the warmth of a sauna? Need your ideas
The pictures are everything.

The Website for our book
https://maplewickvigor.com/

Coding

Coded - Design and coding required

Number of Pages Required

1 page

Requirements
Must have
• Great pictures

```html
<!DOCTYPE html>
<html lang="en">
<head>
<meta charset="utf-8">
<title>Maplewick Vigor Fitness for Men</title>
<link href="https://fonts.googleapis.com/css2?family=Roboto+Condensed:wght@400;700&family=Roboto:ital,wght@0,400;0,500;0,700;1,400&display=swap" rel="stylesheet">
<style>
:root{
  --orange:#e8771f;
  --orange-soft:#fdf0e6;
  --ink:#111111;
  --dark:#0d0d10;
  --grey:#6d6d6d;
  --about-bg:#d4d9d7;
  --white:#ffffff;
}
*{margin:0;padding:0;box-sizing:border-box}
html,body{width:1200px;height:4938px;overflow:hidden}
body{font-family:'Roboto',Arial,sans-serif;color:var(--ink);background:var(--white);position:relative}
.heading{font-family:'Roboto Condensed',Arial Narrow,sans-serif;font-weight:700;text-transform:uppercase}
section,header,footer{position:absolute;left:0;width:1200px}

/* hero */
.hero{top:0;height:683px;background:linear-gradient(100deg,#3a2416 0%,#7a4a2a 35%,#a8683a 60%,#5a3620 100%);overflow:hidden}
.hero-photo{position:absolute;inset:0}
.hero-shade{position:absolute;inset:0;background:linear-gradient(90deg,rgba(0,0,0,.45) 0%,rgba(0,0,0,.15) 50%,rgba(0,0,0,0) 100%)}
.brand-mark{position:absolute;top:30px;left:50%;transform:translateX(-50%);display:flex;flex-direction:column;align-items:center;gap:8px}
.brand-mark .dot{width:54px;height:54px;border-radius:50%;border:3px solid var(--white)}
.brand-mark .name{font-family:'Roboto',Arial,sans-serif;font-weight:700;font-size:15px;color:var(--white);text-align:center;width:160px;line-height:1.2}
.hero-copy{position:absolute;left:77px;top:160px;color:var(--white)}
.hero-tag{font-size:16px;line-height:30px}
.hero-title{font-size:43px;line-height:51px;margin-top:20px}
.hero-sub{font-size:20px;line-height:30px;margin-top:20px}

/* circulation band */
.circulation{top:683px;height:253px;background:var(--orange);color:var(--white);text-align:center}
.circulation h2{font-size:41px;margin-top:78px}
.circulation p{font-family:'Roboto Condensed',sans-serif;font-weight:700;font-size:18px;margin-top:8px;text-transform:uppercase}

/* benefits */
.benefits{top:936px;height:626px;text-align:center}
.benefits h2{font-size:42px;line-height:51px;margin-top:80px}
.benefit-list{position:absolute;top:270px;left:111px;display:flex;gap:29px}
.benefit{width:222px;height:195px;background:var(--orange-soft);display:flex;flex-direction:column;align-items:center;padding-top:28px}
.benefit svg{width:76px;height:76px}
.benefit span{font-size:20px;line-height:25px;margin-top:18px;color:#222}
.arrow{position:absolute;top:360px;width:20px;height:20px}
.arrow.prev{left:42px}.arrow.next{left:1133px}
.benefits .note{position:absolute;top:504px;width:100%;font-family:'Roboto Condensed',sans-serif;font-weight:700;font-size:19px}

/* blood flow */
.bloodflow{top:1562px;height:420px;background:radial-gradient(ellipse at 30% 30%,#2a2a2c 0%,#111 55%,#050505 100%);text-align:center}
.bloodflow-photo{position:absolute;inset:0}
.bloodflow h2{position:relative;font-size:64px;line-height:77px;margin-top:102px;color:transparent;-webkit-text-stroke:2px #f1f1f1;letter-spacing:1px}

/* about */
.about{top:1982px;height:571px;background:var(--about-bg)}
.about-photo{position:absolute;left:0;top:0;width:600px;height:571px;background:linear-gradient(90deg,#ded7cc 0%,#c9c3b9 55%,rgba(212,217,215,0) 100%)}
.about-copy{position:absolute;left:600px;top:100px;width:490px}
.about-copy h2{font-size:39px}
.about-copy p{font-size:13.5px;line-height:21.5px;color:#6a6a6a;text-align:justify;margin-top:10px}
.about-copy p + p{margin-top:21px}

/* products */
.products{top:2553px;height:1300px;text-align:center}
.products > h2{font-size:42px;margin-top:100px}
.products > .lead{font-size:13.5px;line-height:21px;color:#555;width:780px;margin:10px auto 0}
.product{position:absolute;left:111px;width:978px;height:326px;background:var(--dark);overflow:hidden;text-align:left}
.product .shape{position:absolute;inset:0}
.product .item{position:absolute;top:26px;width:260px;height:274px;border-radius:6px}
.product .info{position:absolute;top:64px;width:410px;color:var(--white)}
.product h3{font-size:35px}
.product p{font-size:13.5px;line-height:21.5px;margin-top:14px}
.buttons{display:flex;gap:14px;margin-top:28px}
.btn{border:2px solid var(--orange);color:var(--orange);font-size:12.5px;font-weight:700;text-transform:uppercase;height:37px;display:flex;align-items:center;justify-content:center;white-space:nowrap;flex:none}
.btn-buy{width:107px}.btn-supplier{width:172px}
.sauna{top:219px}.plunge{top:562px}.chairs{top:905px}

/* testimonials */
.testimonials{top:3853px;height:537px}
.testimonials h2{font-size:42px;text-align:center;margin-top:60px}
.quote{position:absolute;top:168px;width:470px}
.quote svg{width:78px;height:52px}
.quote p{font-style:italic;font-size:13.5px;line-height:25px;color:#777;margin-top:20px}
.quote.one{left:111px}.quote.two{left:625px}
.pager{position:absolute;top:378px;left:554px;display:flex;gap:10px}
.pager span{width:38px;height:38px;border-radius:50%;background:#e4e4e4;display:flex;align-items:center;justify-content:center}

/* footer */
.site-footer{top:4390px;height:548px;background:radial-gradient(ellipse at 50% 40%,#1e1e1e 0%,#080808 60%,#000 100%);color:var(--white)}
.footer-mark{top:90px}
.contacts{position:absolute;top:290px;left:0;width:100%}
.contact-item{position:absolute;display:flex;gap:22px}
.contact-item .icon{width:46px;height:46px;border-radius:50%;background:var(--orange);display:flex;align-items:center;justify-content:center;flex:none}
.contact-item h4{font-size:20px;font-weight:500}
.contact-item p{font-size:13.5px;line-height:25px;margin-top:2px;width:170px}
.contact-item.addr{left:217px}.contact-item.mail{left:491px}.contact-item.phone{left:824px}
.socials{position:absolute;top:382px;left:537px;display:flex;gap:7px}
.socials span{width:26px;height:26px;border-radius:50%;border:1.5px solid var(--white)}
.copyright{position:absolute;top:428px;width:100%;text-align:center;font-size:13.5px}
</style>
</head>
<body>

<header class="hero">
  <div class="hero-photo" role="img" aria-label="Couple in white robes relaxing together on the wooden benches of a warm sauna"></div>
  <div class="hero-shade"></div>
  <div class="brand-mark"><span class="dot"></span><span class="name">Maplewick Vigor Fitness for Men</span></div>
  <div class="hero-copy">
    <p class="hero-tag">Maplewick Vigor Fitness for Men<br>Top of the Line Health Products Exclusively<br>for the Financially Successful</p>
    <h1 class="heading hero-title">Dramatically<br>Improve Your Health<br>Without Exercise</h1>
    <p class="hero-sub">Successful Men Recognize the Importance<br>of Their Health and Make it a Priority.<br>It's Your Time.&nbsp; You've Earned it.</p>
  </div>
</header>

<section class="circulation">
  <h2 class="heading">A Mans Body Thrives on Circulation</h2>
  <p>And it doesn't care how you get it.</p>
</section>

<section class="benefits">
  <h2 class="heading">When There's No Time for Exercise.<br>Use Hot, Cold, or Massage.<br>The Benefits Are Numerous.</h2>
  <svg class="arrow prev" viewBox="0 0 20 20"><path d="M13 3 6 10l7 7" fill="none" stroke="#111" stroke-width="2"/></svg>
  <div class="benefit-list">
    <div class="benefit">
      <svg viewBox="0 0 76 76"><path d="M38 6c-16 0-26 11-26 25 0 8 3 13 7 17v22h26v-9h10c3 0 5-2 5-5v-9l5-2-6-10c0-17-9-29-21-29z" fill="var(--orange)"/><path d="M28 24h6v6h-6zM38 24h6v6h-6zM28 34h6v6h-6zM38 34h6v6h-6z" fill="var(--white)"/></svg>
      <span>Relieve Stress</span>
    </div>
    <div class="benefit">
      <svg viewBox="0 0 76 76"><path d="M18 8h40l-4 30 8 30H14l8-30z" fill="var(--orange)"/><circle cx="38" cy="28" r="11" fill="none" stroke="var(--white)" stroke-width="5"/></svg>
      <span>Detox Your Pores</span>
    </div>
    <div class="benefit">
      <svg viewBox="0 0 76 76"><rect x="8" y="30" width="6" height="38" fill="var(--orange)"/><circle cx="24" cy="42" r="6" fill="var(--orange)"/><rect x="14" y="50" width="56" height="10" fill="var(--orange)"/><rect x="32" y="40" width="34" height="10" rx="3" fill="var(--orange)"/><rect x="64" y="50" width="6" height="18" fill="var(--orange)"/><path d="M44 10h10l-10 12h10M58 4h7l-7 8h7" fill="none" stroke="var(--orange)" stroke-width="3"/></svg>
      <span>Sleep Better</span>
    </div>
    <div class="benefit">
      <svg viewBox="0 0 76 76"><path d="M28 6h20l16 10 4 44h-10l-2-30v40H20V30l-2 30H8l4-44z" fill="var(--orange)"/><path d="M30 22v10M26 28l4 4 4-4M46 22v10M42 28l4 4 4-4M38 52V42M34 46l4-4 4 4" fill="none" stroke="var(--white)" stroke-width="2.5"/></svg>
      <span>Relieve Muscle<br>Tension</span>
    </div>
  </div>
  <svg class="arrow next" viewBox="0 0 20 20"><path d="M7 3l7 7-7 7" fill="none" stroke="#111" stroke-width="2"/></svg>
  <p class="note">SPECIFIC IMPROVEMENTS WILL BE INDIVIDUAL TO YOU.</p>
</section>

<section class="bloodflow">
  <div class="bloodflow-photo" role="img" aria-label="Dark moody gym scene with a muscular figure and a dumbbell"></div>
  <h2 class="heading">Everything Works<br>Better With Increased<br>Blood Flow</h2>
</section>

<section class="about">
  <div class="about-photo" role="img" aria-label="Woman reading a magazine while relaxing in a white massage chair by a bright window"></div>
  <div class="about-copy">
    <h2 class="heading">About Us</h2>
    <p>Lorem ipsum dolor sit amet, consectetur adipiscing elit, sed do eiusmod tempor incididunt ut labore et dolore magna aliqua. Ut enim ad minim veniam, quis nostrud exercitation ullamco laboris nisi ut aliquip ex ea commodo consequat. Duis aute irure dolor in reprehenderit in voluptate velit esse cillum dolore eu fugiat nulla pariatur.</p>
    <p>Excepteur sint occaecat cupidatat non proident, sunt in culpa qui officia deserunt mollit anim id est laborum. Lorem ipsum dolor sit amet, consectetur adipiscing elit, sed do eiusmod tempor incididunt ut labore et dolore magna aliqua. Ut enim ad minim veniam, quis nostrud exercitation ullamco laboris nisi ut aliquip ex ea commodo consequat. Duis aute irure dolor in reprehenderit in voluptate velit esse cillum dolore eu fugiat nulla pariatur. Excepteur sint occaecat cupidatat non proident, sunt in culpa qui officia deserunt mollit anim id est laborum.</p>
  </div>
</section>

<section class="products">
  <h2 class="heading">Our Products</h2>
  <p class="lead">Lorem ipsum dolor sit amet, consectetur adipiscing elit, sed do eiusmod tempor incididunt ut labore et dolore magna aliqua. Ut enim ad minim veniam, quis nostrud exercitation ullamco laboris nisi</p>

  <article class="product sauna">
    <svg class="shape" viewBox="0 0 978 326" preserveAspectRatio="none"><polygon points="886,0 978,0 978,326 575,326" fill="var(--orange)"/></svg>
    <div class="item" style="left:630px;background:linear-gradient(135deg,#d79a5e,#9c5a2c)" role="img" aria-label="Wooden indoor sauna cabin with glass door"></div>
    <div class="info" style="left:69px">
      <h3 class="heading">Saunas</h3>
      <p>Lorem ipsum dolor sit amet, consectetur adipiscing elit, sed do eiusmod tempor incididunt ut labore et dolore magna aliqua. Ut enim ad minim veniam, quis nostrud exercitation ullamco laboris nisi ut aliquip ex ea commodo consequat.</p>
      <div class="buttons"><span class="btn btn-buy">Buy Now</span><span class="btn btn-supplier">Contact Supplier</span></div>
    </div>
  </article>

  <article class="product plunge">
    <svg class="shape" viewBox="0 0 978 326" preserveAspectRatio="none"><polygon points="0,0 400,0 400,170 230,326 0,326" fill="var(--orange)"/></svg>
    <div class="item" style="left:110px;background:linear-gradient(135deg,#8a5232,#4a2818)" role="img" aria-label="Round wooden cold plunge barrel tub"></div>
    <div class="info" style="left:519px">
      <h3 class="heading">Cold Plunge Tubs</h3>
      <p>Lorem ipsum dolor sit amet, consectetur adipiscing elit, sed do eiusmod tempor incididunt ut labore et dolore magna aliqua. Ut enim ad minim veniam, quis nostrud exercitation ullamco laboris nisi ut aliquip ex ea commodo consequat.</p>
      <div class="buttons"><span class="btn btn-buy">Buy Now</span><span class="btn btn-supplier">Contact Supplier</span></div>
    </div>
  </article>

  <article class="product chairs">
    <svg class="shape" viewBox="0 0 978 326" preserveAspectRatio="none"><polygon points="860,0 978,0 978,326 575,326" fill="var(--orange)"/></svg>
    <div class="item" style="left:630px;background:linear-gradient(135deg,#3a3a3e,#151517)" role="img" aria-label="Black reclining full body massage chair"></div>
    <div class="info" style="left:69px">
      <h3 class="heading">Massage Chairs</h3>
      <p>Lorem ipsum dolor sit amet, consectetur adipiscing elit, sed do eiusmod tempor incididunt ut labore et dolore magna aliqua. Ut enim ad minim veniam, quis nostrud exercitation ullamco laboris nisi ut aliquip ex ea commodo consequat.</p>
      <div class="buttons"><span class="btn btn-buy">Buy Now</span><span class="btn btn-supplier">Contact Supplier</span></div>
    </div>
  </article>
</section>

<section class="testimonials">
  <h2 class="heading">Testimonials</h2>
  <div class="quote one">
    <svg viewBox="0 0 78 52"><path d="M4 30c0-16 8-26 20-30l3 6c-7 3-10 8-10 14 9 0 14 6 14 15s-6 17-14 17C10 52 4 44 4 30zM44 30c0-16 8-26 20-30l3 6c-7 3-10 8-10 14 9 0 14 6 14 15s-6 17-14 17c-7 0-13-8-13-22z" fill="var(--orange)"/></svg>
    <p>"I climb in my sauna half asleep every morning for 20 minutes before I take a shower and head off to work. It's the only thing I found that really wakes me up in the morning. I'm not a coffee drinker so that's never been an option but this sauna is the perfect morning wake up."</p>
  </div>
  <div class="quote two">
    <svg viewBox="0 0 78 52"><path d="M4 30c0-16 8-26 20-30l3 6c-7 3-10 8-10 14 9 0 14 6 14 15s-6 17-14 17C10 52 4 44 4 30zM44 30c0-16 8-26 20-30l3 6c-7 3-10 8-10 14 9 0 14 6 14 15s-6 17-14 17c-7 0-13-8-13-22z" fill="var(--orange)"/></svg>
    <p>"I love a good massage but making an appointment is almost impossible with my schedule.&nbsp; The chair is always there.&nbsp; I climb in and let it do its thing.&nbsp; I forget about work so much that it usually turns in to a power nap."</p>
  </div>
  <div class="pager">
    <span><svg width="12" height="12" viewBox="0 0 12 12"><path d="M8 2 4 6l4 4" fill="none" stroke="#333" stroke-width="1.6"/></svg></span>
    <span><svg width="12" height="12" viewBox="0 0 12 12"><path d="M4 2l4 4-4 4" fill="none" stroke="#333" stroke-width="1.6"/></svg></span>
  </div>
</section>

<footer class="site-footer">
  <div class="brand-mark footer-mark"><span class="dot"></span><span class="name">Maplewick Vigor Fitness for Men</span></div>
  <div class="contacts">
    <div class="contact-item addr">
      <span class="icon"><svg width="18" height="22" viewBox="0 0 18 22"><path d="M9 1a8 8 0 0 0-8 8c0 6 8 12 8 12s8-6 8-12a8 8 0 0 0-8-8z" fill="#fff"/><circle cx="9" cy="9" r="3" fill="var(--orange)"/></svg></span>
      <div><h4>Address :</h4><p>123, Lorem ipsum dolor amet, consectetur</p></div>
    </div>
    <div class="contact-item mail">
      <span class="icon"><svg width="20" height="16" viewBox="0 0 20 16"><rect x="1" y="1" width="18" height="14" rx="2" fill="#fff"/><path d="M1 3l9 6 9-6" fill="none" stroke="var(--orange)" stroke-width="1.6"/></svg></span>
      <div><h4>Email Address :</h4><p>info@maplewickvigor.com</p></div>
    </div>
    <div class="contact-item phone">
      <span class="icon"><svg width="20" height="20" viewBox="0 0 20 20"><path d="M4 1l4 4-2 3c1 2 3 4 6 6l3-2 4 4-3 3C9 19 1 11 1 4z" fill="#fff"/></svg></span>
      <div><h4>Phone :</h4><p>+1 888 888 8888</p></div>
    </div>
  </div>
  <div class="socials"><span></span><span></span><span></span><span></span></div>
  <p class="copyright">Copyright © 2024. All Rights Reserved</p>
</footer>

</body>
</html>
```